Young Accounting firm needing a captivating business card

We need a business card design that forces the person to look at the card because its either gold foil, plastic, or lettering pop up etc. We already have a logo with a specific gold color and we need to make it pop. We are an accounting firm. I need the words" accounting, payroll, licenses, audits, taxes" somewhere on the business card so as to describe what we do- preferably on the side where the logo is at.

Industry/Entity Type

Accounting

Contact Information for Business Card

Address 48276 9th Ave S Ste 305, Federal Way, WA 98117
Business Phone (360)418-2096
Fax (360)418-2157
Office Cell Phone (360)586-7319

Font styles to use
Serif

Colors
85abd2

Requirements
Must have
• It should state
• "Accounting" "Taxes" "Audits" "Licenses" "Payroll"
Nice to have
• Matte with gold foil, different textures, With Either a textured ivory background or gray blue slate background
Should not have
• colorful colors

```html
<!DOCTYPE html>
<html lang="en">
<head>
<meta charset="utf-8">
<title>Aurelan Tax – Business Card</title>
<link rel="stylesheet" href="https://fonts.googleapis.com/css2?family=Lato:wght@400;900&display=swap">
<style>
  :root {
    --gold: #bd992f;
    --gold-light: #e3c46f;
    --ink: #5f5f5f;
    --paper: #ffffff;
    --backdrop: #e6e3df;
    --tagline: #f1e6c4;
  }
  html, body {
    margin: 0;
    width: 1200px;
    height: 800px;
    overflow: hidden;
    background: var(--backdrop);
    font-family: "Lato", Arial, sans-serif;
  }
  .canvas { position: relative; width: 1200px; height: 800px; }
  .card {
    position: absolute;
    left: 356px;
    width: 493px;
    height: 282px;
    border-radius: 20px;
    overflow: hidden;
  }
  .card--front { top: 80px; background: var(--paper); }
  .card--back { top: 433px; background: var(--gold); }

  .front-band { position: absolute; inset: 0; }

  .brand { position: absolute; text-align: center; }
  .brand__mark { display: block; margin: 0 auto; border-radius: 50%; }
  .brand__name { display: block; font-weight: 400; white-space: nowrap; letter-spacing: -0.5px; }

  .card--front .brand { left: 30px; top: 81px; width: 206px; }
  .card--front .brand__mark { width: 52px; height: 52px; background: var(--gold); }
  .card--front .brand__name { color: var(--gold); font-size: 30px; margin-top: 12px; }

  .divider {
    position: absolute; left: 246px; top: 55px;
    width: 1px; height: 141px; background: var(--gold);
  }
  .contact { position: absolute; left: 263px; top: 46px; color: var(--ink); }
  .contact__name { margin: 0; color: var(--gold); font-weight: 900; font-size: 22px; line-height: 26px; }
  .contact__role { margin: 0; font-size: 12px; line-height: 15px; }
  .contact__address { margin: 6px 0 0; font-size: 12px; line-height: 15px; font-style: normal; }
  .contact__list { list-style: none; margin: 9px 0 0; padding: 0; font-size: 12px; }
  .contact__list li { display: flex; align-items: center; height: 17.3px; }
  .contact__list svg { width: 11px; height: 11px; margin-right: 8px; fill: var(--gold); }

  .card--back .brand { left: 0; right: 0; top: 82px; }
  .card--back .brand__mark { width: 76px; height: 76px; background: var(--paper); }
  .card--back .brand__name { color: var(--paper); font-size: 44px; margin-top: 8px; line-height: 48px; }
  .services {
    position: absolute; left: 0; right: 0; top: 202px;
    text-align: center; color: var(--tagline); font-size: 11.5px; letter-spacing: 0.2px;
  }
  .services span { margin: 0 4px; }
</style>
</head>
<body>
<div class="canvas">

  <section class="card card--front">
    <svg class="front-band" viewBox="0 0 493 282" width="493" height="282" aria-hidden="true">
      <path d="M26 211 Q246 264 465 208" fill="none" stroke="var(--gold-light)" stroke-width="2"/>
      <path d="M0 213 Q246 282 493 208 L493 282 L0 282 Z" fill="var(--gold)"/>
    </svg>

    <div class="brand">
      <span class="brand__mark"></span>
      <span class="brand__name">Aurelan Tax</span>
    </div>

    <div class="divider"></div>

    <div class="contact">
      <h1 class="contact__name">Daniel Reyes</h1>
      <p class="contact__role">Founder</p>
      <address class="contact__address">48276 9th Ave S Ste 305,<br>Federal Way, WA 98117</address>
      <ul class="contact__list">
        <li><svg viewBox="0 0 12 12"><path d="M3 0h6a1 1 0 0 1 1 1v10a1 1 0 0 1-1 1H3a1 1 0 0 1-1-1V1a1 1 0 0 1 1-1zm0 1.5v8h6v-8zM5.5 10.2h1v.8h-1z"/></svg>(360) 586-7319</li>
        <li><svg viewBox="0 0 12 12"><path d="M0 4c2-3 10-3 12 0v1.5H9V4H3v1.5H0zM2 6h8l1 5H1zm4 1.2a1.6 1.6 0 1 0 0 3.2 1.6 1.6 0 0 0 0-3.2z"/></svg>(360) 418-2096</li>
        <li><svg viewBox="0 0 12 12"><path d="M3 0h6v3H3zM0 4h12v5h-2V7H2v2H0zM3 8h6v4H3z"/></svg>(360) 418-2157</li>
        <li><svg viewBox="0 0 12 12"><path d="M0 2h12v1L6 7 0 3zm0 2.2 6 4 6-4V10H0z"/></svg>daniel@aurelanmail.com</li>
      </ul>
    </div>
  </section>

  <section class="card card--back">
    <div class="brand">
      <span class="brand__mark"></span>
      <span class="brand__name">Aurelan Tax</span>
    </div>
    <p class="services">Accounting<span>|</span>Taxes<span>|</span>Audits<span>|</span>Licenses<span>|</span>Payroll</p>
  </section>

</div>
</body>
</html>
```